Business Card for Voltrix

Horizontal business card for voltrix, the electrical contractor.
clean and professional looking, using company branding and colours.
I also want the blue in the logo and wording to be made a more 'electric' blue and the grey 'Voltrix' to be slightly darker.

Pleas use the following contact details:

Colin Marsh
Owner

t: 01736 582910
m: 07831 206719
e: colin@voltrix-installs.co.uk

www.voltrix-installs.co.uk

Industry/Entity Type

Electrical

Font styles to use
Sans Serif

```html
<!DOCTYPE html>
<html lang="en">
<head>
<meta charset="utf-8">
<title>Voltrix – Business Card</title>
<link rel="stylesheet" href="https://fonts.googleapis.com/css2?family=Abel&family=Roboto:wght@300&display=swap">
<style>
  :root {
    --electric-blue: #1cc6ec;
    --charcoal: #45484a;
    --slate: #737779;
    --wordmark-grey: #3d4042;
    --card-white: #ffffff;
    --backdrop: #e9e9ec;
    --contact-text: #f2f4f5;
  }
  * { box-sizing: border-box; margin: 0; padding: 0; }
  html, body {
    width: 1200px;
    height: 900px;
    overflow: hidden;
    background: var(--backdrop);
  }
  .canvas {
    width: 1200px;
    height: 900px;
    display: flex;
    align-items: center;
    justify-content: center;
    gap: 40px;
  }
  .card {
    position: relative;
    width: 540px;
    height: 310px;
    overflow: hidden;
    box-shadow: 0 6px 18px rgba(0,0,0,0.22);
  }
  .card-decor {
    position: absolute;
    inset: 0;
    width: 100%;
    height: 100%;
  }

  /* Front */
  .card-front { background: var(--card-white); }
  .brand {
    position: absolute;
    left: 86px;
    top: 222px;
    display: flex;
    align-items: center;
    gap: 14px;
  }
  .brand-dot {
    width: 34px;
    height: 34px;
    border-radius: 50%;
    background: var(--electric-blue);
  }
  .brand-name {
    font-family: "Abel", sans-serif;
    font-size: 44px;
    line-height: 1;
    color: var(--wordmark-grey);
  }

  /* Back */
  .card-back { background: var(--slate); }
  .contact {
    position: absolute;
    left: 318px;
    top: 34px;
    color: var(--contact-text);
  }
  .contact-name {
    font-family: "Abel", sans-serif;
    font-weight: 400;
    font-size: 34px;
    color: var(--card-white);
    margin-bottom: 12px;
    white-space: nowrap;
  }
  .contact-list { list-style: none; }
  .contact-item {
    display: flex;
    align-items: center;
    gap: 8px;
    font-family: "Roboto", sans-serif;
    font-weight: 300;
    font-size: 12.5px;
    height: 22px;
    white-space: nowrap;
  }
  .contact-icon {
    width: 14px;
    height: 14px;
    flex: none;
    fill: none;
    stroke: var(--contact-text);
    stroke-width: 1.4;
  }
  .contact-icon .solid { fill: var(--contact-text); stroke: none; }
</style>
</head>
<body>
<main class="canvas">

  <section class="card card-front" aria-label="Business card front">
    <svg class="card-decor" viewBox="0 0 540 310" role="img" aria-label="Decorative curved colour bands across the top corner">
      <defs>
        <linearGradient id="front-band" x1="0" y1="0" x2="1" y2="0.6">
          <stop offset="0" stop-color="var(--charcoal)"/>
          <stop offset="0.55" stop-color="var(--electric-blue)"/>
          <stop offset="1" stop-color="var(--electric-blue)"/>
        </linearGradient>
      </defs>
      <path fill="url(#front-band)" d="M0,0 H540 V36 Q250,44 0,212 Z"/>
    </svg>
    <div class="brand">
      <span class="brand-dot" aria-hidden="true"></span>
      <span class="brand-name">Voltrix</span>
    </div>
  </section>

  <section class="card card-back" aria-label="Business card back">
    <svg class="card-decor" viewBox="0 0 540 310" role="img" aria-label="Decorative curved colour band along the left edge">
      <defs>
        <linearGradient id="back-band" x1="0" y1="1" x2="1" y2="0">
          <stop offset="0" stop-color="var(--charcoal)"/>
          <stop offset="0.45" stop-color="var(--electric-blue)"/>
          <stop offset="1" stop-color="var(--electric-blue)"/>
        </linearGradient>
      </defs>
      <path fill="url(#back-band)" d="M0,0 H34 Q170,240 412,310 H0 Z"/>
    </svg>
    <div class="contact">
      <h1 class="contact-name">Colin Marsh</h1>
      <ul class="contact-list">
        <li class="contact-item">
          <svg class="contact-icon" viewBox="0 0 14 14" aria-hidden="true"><path class="solid" d="M3,1 L5,1 L6,4 L4.6,5.2 Q6,8.2 8.8,9.4 L10,8 L13,9 L13,11 Q12,13 10,13 Q2,11 1,3 Q1,1 3,1 Z"/></svg>
          01736 582910
        </li>
        <li class="contact-item">
          <svg class="contact-icon" viewBox="0 0 14 14" aria-hidden="true"><rect x="3.5" y="0.8" width="7" height="12.4" rx="1.2"/><line x1="6" y1="11" x2="8" y2="11"/></svg>
          07831 206719
        </li>
        <li class="contact-item">
          <svg class="contact-icon" viewBox="0 0 14 14" aria-hidden="true"><rect class="solid" x="1" y="3" width="12" height="8"/><path d="M1,3 L7,7.5 L13,3" stroke="var(--slate)"/></svg>
          colin@voltrix-installs.co.uk
        </li>
        <li class="contact-item">
          <svg class="contact-icon" viewBox="0 0 14 14" aria-hidden="true"><circle cx="7" cy="7" r="6"/><ellipse cx="7" cy="7" rx="2.6" ry="6"/><line x1="1" y1="7" x2="13" y2="7"/></svg>
          www.voltrix-installs.co.uk
        </li>
      </ul>
    </div>
  </section>

</main>
</body>
</html>
```